Hair Salon Brochure

We need a brochure for our hair salon located in Middle Tennessee called Delphine Locks of Harbor Bend. Along with standard services, we offer specialized services and accommodations for individuals on the Autism Spectrum, regardless of background or hair type.
At Delphine Locks of Harbor Bend, our mission is to create a warm and inclusive haven for individuals of all backgrounds, including those on the autism spectrum and their families. We are dedicated to providing not only exceptional hairstyling services but also hands-on education and specialized cutting techniques for clients with natural textured hair. Our goal is to empower our clients with the knowledge and tools necessary to maintain a successful hair care routine, ensuring they leave our salon feeling confident.
We believe in fostering a sense of community, where parents of younger clients are encouraged to learn the proper hair care techniques for their children, promoting healthy practices at home. Our commitment extends beyond just hair; we are here to help you embrace your true self and recognize the beauty that resides within.
At Delphine Locks of Harbor Bend, our passion is to deliver the ultimate client experience, where you can be unapologetically yourself and feel completely at ease. From the moment you step through our doors, you are welcomed not only to discuss your hair concerns but also to engage in meaningful conversations about life. Together, we will collaborate on a personalized plan to achieve your hair goals and transform the way you perceive yourself.
Always remember, when you look good, you feel good, and when you feel good, you can achieve great things. We firmly believe that every individual is 'Beautiful Beyond the Spectrum,' and we are here to celebrate that beauty with you."
https://www.delphinelocks.net/
Tagline - "Beautiful Beyond the Spectrum"

```html
<!DOCTYPE html>
<html lang="en">
<head>
<meta charset="utf-8">
<title>Delphine Locks of Harbor Bend – Brochure</title>
<link href="https://fonts.googleapis.com/css2?family=Great+Vibes&family=Lobster&family=Open+Sans:wght@400;600;700;800&display=swap" rel="stylesheet">
<style>
:root{
  --navy:#1e2468;
  --purple:#4b2a8c;
  --violet:#6a3fb0;
  --orange:#f0821c;
  --blue:#2b5bc4;
  --ink:#2d2d3a;
  --white:#ffffff;
  --page:#ffffff;
}
*{margin:0;padding:0;box-sizing:border-box}
html,body{width:876px;height:1200px;overflow:hidden;background:var(--page)}
body{position:relative;font-family:"Open Sans",Arial,sans-serif;color:var(--ink)}
.spread{position:absolute;left:30px;width:816px;background:var(--white);box-shadow:0 3px 10px rgba(0,0,0,.25);overflow:hidden}
.spread--outside{top:22px;height:525px}
.spread--inside{top:588px;height:545px}
.spread-shapes{position:absolute;inset:0}
.panel{position:absolute;top:0;width:272px;height:100%;padding:22px 22px}
.panel--left{left:0}.panel--mid{left:272px}.panel--right{left:544px}
.brand{font-family:"Lobster",cursive;color:var(--purple);font-size:19px;line-height:1.05}
.script-head{font-family:"Lobster",cursive;color:var(--orange);font-size:22px;margin:14px 0 6px;line-height:1.25}
.body-copy{font-size:7.4px;line-height:1.5;margin-bottom:7px}
.contact-line{font-size:9px;color:var(--blue);font-weight:600;line-height:1.5}
.photo{position:absolute;border-radius:0 0 0 130px;background:radial-gradient(circle at 45% 45%,#b08a74 0%,#5b4034 45%,#2a2230 100%)}
.tagline-big{font-family:"Great Vibes",cursive;color:var(--purple);font-size:44px;line-height:1}
.tagline-small{font-family:"Great Vibes",cursive;color:var(--orange);font-size:28px;line-height:1;margin-bottom:10px}
.book{text-align:center;font-weight:800;color:var(--navy);font-size:11px;margin-top:8px}
.book span{display:block;font-size:13px}
.service-list{list-style:none}
.service-list li{color:var(--white);font-weight:700;font-size:12.5px;line-height:1.35;padding:5px 0;border-bottom:1px solid rgba(255,255,255,.25)}
.brand-lockup{position:absolute;left:22px;bottom:30px;right:22px;display:flex;align-items:center;gap:12px}
.brand-lockup .dot{width:54px;height:54px;border-radius:50%;background:var(--orange);flex:none}
.brand-lockup .brand{color:var(--white);font-size:22px}
.signoff{position:absolute;right:22px;bottom:28px;text-align:right;font-size:10px;font-weight:700;color:var(--navy);line-height:1.5}
.signoff--left{left:22px;right:auto;text-align:left;bottom:34px}
</style>
</head>
<body>

<section class="spread spread--outside">
  <svg class="spread-shapes" viewBox="0 0 816 525" aria-hidden="true">
    <path d="M272 525 L272 470 C380 420 480 420 560 445 C640 470 720 465 816 430 L816 525 Z" fill="var(--navy)"/>
    <path d="M272 490 C370 450 470 455 560 475 L560 525 L272 525 Z" fill="var(--purple)"/>
    <path d="M272 450 C380 400 480 400 560 425 C640 450 720 445 816 410" fill="none" stroke="var(--orange)" stroke-width="4"/>
  </svg>

  <div class="panel panel--left">
    <div class="brand">Delphine Locks<br>of Harbor Bend</div>
    <h2 class="script-head">Our mission</h2>
    <p class="body-copy">At Delphine Locks of Harbor Bend, our mission is to create a warm and inclusive haven for individuals of all backgrounds, including those on the autism spectrum and their families. We are dedicated to exceptional styling, hands-on education and specialized cutting techniques for natural textured hair.</p>
    <p class="body-copy">We believe in fostering community, where parents of younger clients learn proper hair care techniques for their children, promoting healthy practices at home. Our commitment extends beyond hair; we help you embrace your true self.</p>
    <p class="body-copy">Our passion is to deliver the ultimate client experience, where you can be unapologetically yourself and feel completely at ease. Together we will build a personalized plan to reach your hair goals.</p>
    <p class="body-copy">Always remember, when you look good, you feel good, and when you feel good, you can achieve great things.</p>
  </div>

  <div class="panel panel--mid">
    <h2 class="script-head" style="margin-top:80px">Contact Us</h2>
    <p class="contact-line">Delphine Locks of Harbor Bend<br>418 Riverside Ave Suite 12<br>Harbor Bend, Tennessee 37190</p>
    <h2 class="script-head" style="font-size:18px">Opening Hours</h2>
    <p class="contact-line">Thursday and Friday: 8:00 am – 1:00 pm<br>Saturday: 7:00 am – 12:00 pm</p>
    <p class="contact-line" style="margin-top:40px">https://www.delphinelocks.net/</p>
  </div>

  <div class="photo" role="img" aria-label="Portrait photograph of the salon owner" style="left:580px;top:0;width:236px;height:225px"></div>

  <div class="panel panel--right" style="padding-top:245px">
    <div class="tagline-big">Beautiful</div>
    <div class="tagline-small">Beyond the Spectrum</div>
    <p class="body-copy">Every individual is beautiful beyond the spectrum, and we are here to celebrate that beauty with you. Book a relaxed visit built around your needs.</p>
    <p class="book">BOOK NOW<span>(615) 555-0148</span></p>
  </div>
</section>

<section class="spread spread--inside">
  <svg class="spread-shapes" viewBox="0 0 816 545" aria-hidden="true">
    <rect x="0" y="0" width="272" height="545" fill="var(--navy)"/>
    <rect x="272" y="0" width="272" height="545" fill="var(--purple)"/>
    <path d="M272 40 C360 10 470 20 544 60 L544 500 C470 530 360 535 272 510 Z" fill="var(--white)"/>
    <path d="M272 30 C360 0 470 10 544 50" fill="none" stroke="var(--orange)" stroke-width="4"/>
  </svg>

  <div class="panel panel--left">
    <h2 class="script-head" style="margin-top:0;font-size:26px">Services</h2>
    <ul class="service-list">
      <li>Specialized Services for Autism Spectrum Individuals</li>
      <li>Warm and Inclusive environment</li>
      <li>Exceptional Hairstyling Services</li>
      <li>Hands-on Education for Natural Textured Hair</li>
      <li>Specialized Cutting Techniques</li>
      <li>Empowerment Through Knowledge and Tools</li>
      <li>Dedication to Client Confidence</li>
    </ul>
    <div class="brand-lockup"><span class="dot"></span><span class="brand">Delphine Locks<br>of Harbor Bend</span></div>
  </div>

  <div class="panel panel--mid" style="padding-top:62px">
    <h2 class="script-head" style="margin-top:0">Special Services</h2>
    <p class="body-copy" style="color:var(--blue);font-weight:700;font-size:9px">We are not just a salon, we are a support.</p>
    <p class="body-copy">Our calm and quiet salon offers low-sensory visits, flexible timing and a patient pace for every guest.</p>
    <p class="body-copy">Parents and caregivers are welcome to stay close, share needs in advance and help shape each appointment.</p>
    <p class="body-copy">With years of experience in textured hair, we adapt every step so clients feel safe and understood.</p>
    <p class="body-copy">Visit soon and discover care made for you.</p>
    <div class="signoff signoff--left">Renée Calloway<br>(615) 555-0148<br>www.delphinelocks.net</div>
  </div>

  <div class="panel panel--right" style="padding-top:62px">
    <h2 class="script-head" style="margin-top:0">Proper hair techniques are our goal</h2>
    <p class="body-copy">Loving your hair with confidence starts with the right routine and simple tools used at home.</p>
    <p class="body-copy">Tired of buying products that end up under the sink? We guide you to what truly works.</p>
    <p class="body-copy">Parents: do you feel overwhelmed about caring for your child's hair? We teach you step by step.</p>
    <p class="body-copy">Feeling like you need a professional stylist to reset? Book your consultation today.</p>
    <p class="body-copy">Every visit includes an open conversation about your goals, your comfort and your care plan.</p>
    <div class="signoff">Lets Chat<br>Renée Calloway<br>(615) 555-0148</div>
  </div>
</section>

</body>
</html>
```